Tending Our Garden eBook Cover Design

I want to deisgn a cover for my eBook (FRONT COVER) and the title is:

Under the Willow Tree; Where I Found My Quiet Strength and Where You Might Too
By KT Dorran

TITLE CHANGED TO: UNDER THE WILLOW TREE; WHERE I FOUND MY QUIET STRENGTH AND WHERE YOU MIGHT TOO

The color palette is attached. Along with some photos options of me. Along with the ebook in WORD Document. My website is www.KTDorranLive.example. You can use a different color palette if you think it is best

Target Market(s)

women who look to build a personal brand

Industry/Entity Type

health and wellness

Requirements
Must have
• the title
Nice to have
• use my picture on the cover; but that is optional
Should not have
• any men

```html
<!DOCTYPE html>
<html lang="en">
<head>
<meta charset="utf-8">
<title>Under the Willow Tree – KT Dorran</title>
<link rel="stylesheet" href="https://fonts.googleapis.com/css2?family=Josefin+Sans:wght@400&family=Antonio:wght@400&family=Montserrat:wght@800&family=Kaushan+Script&display=swap">
<style>
  :root {
    --page: #ffffff;
    --ink: #0d0d0d;
    --paper: #f3efef;
    --blush: #f9d3df;
    --rose: #f7336f;
    --leaf: #2f9d45;
    --leaf-deep: #1f7a33;
    --hair: #1c1412;
    --top-red: #f0201a;
    --script: #ffffff;
  }
  html, body {
    margin: 0;
    padding: 0;
    width: 1200px;
    height: 2221px;
    overflow: hidden;
    background: var(--page);
  }
  .cover {
    position: absolute;
    left: 220px;
    top: 730px;
    width: 760px;
    height: 760px;
    overflow: hidden;
    background: linear-gradient(90deg, var(--paper) 0%, #fbf3f5 45%, var(--blush) 100%);
    box-shadow: 0 10px 22px rgba(0,0,0,0.25);
  }
  .cover__splash {
    position: absolute;
    inset: 0;
    background:
      radial-gradient(ellipse 260px 300px at 10% 70%, rgba(47,157,69,0.95) 0%, rgba(47,157,69,0.6) 45%, rgba(47,157,69,0) 100%),
      radial-gradient(ellipse 180px 200px at 0% 60%, rgba(31,122,51,0.9) 0%, rgba(31,122,51,0) 100%),
      radial-gradient(ellipse 280px 320px at 92% 66%, rgba(247,51,111,0.95) 0%, rgba(247,51,111,0.55) 45%, rgba(247,51,111,0) 100%),
      radial-gradient(ellipse 220px 240px at 50% 62%, rgba(255,255,255,0.95) 0%, rgba(255,255,255,0) 100%);
  }
  .cover__title {
    position: absolute;
    left: 0;
    right: 0;
    top: 82px;
    text-align: center;
    color: var(--ink);
    margin: 0;
    font-weight: normal;
    white-space: nowrap;
  }
  .title__lead {
    display: block;
    font-family: "Josefin Sans", sans-serif;
    font-size: 38px;
    line-height: 46px;
    letter-spacing: 2px;
  }
  .title__middle {
    display: block;
    font-family: "Antonio", sans-serif;
    font-size: 66px;
    line-height: 74px;
    letter-spacing: -0.5px;
  }
  .title__key {
    display: block;
    font-family: "Montserrat", sans-serif;
    font-weight: 800;
    font-size: 88px;
    line-height: 92px;
    letter-spacing: -4px;
  }
  .title__sub {
    display: block;
    margin-top: 6px;
    font-family: "Josefin Sans", sans-serif;
    font-size: 23px;
    line-height: 28px;
    letter-spacing: 3px;
  }
  .cover__portrait {
    position: absolute;
    left: 207px;
    top: 397px;
    width: 353px;
    height: 363px;
    border-radius: 150px 150px 20px 20px;
    background: linear-gradient(180deg, var(--hair) 0%, #3a2a24 40%, var(--top-red) 72%, var(--top-red) 100%);
  }
  .cover__author {
    position: absolute;
    left: 0;
    right: 0;
    top: 690px;
    text-align: center;
    font-family: "Kaushan Script", cursive;
    font-size: 38px;
    letter-spacing: 3px;
    color: var(--script);
    margin: 0;
  }
</style>
</head>
<body>
  <main class="cover">
    <div class="cover__splash" role="img" aria-label="Painted burst of green leaves on the left and pink leaves on the right"></div>
    <h1 class="cover__title">
      <span class="title__lead">UNDER THE WILLOW TREE;</span>
      <span class="title__middle">WHERE I FOUND MY QUIET</span>
      <span class="title__key">STRENGTH.</span>
      <span class="title__sub">AND WHERE YOU MIGHT TOO</span>
    </h1>
    <div class="cover__portrait" role="img" aria-label="Portrait photo of the author with long dark hair, wearing a red top"></div>
    <p class="cover__author">KT Dorran</p>
  </main>
</body>
</html>
```